Venna coffee business card

a business card for a cofee van business

similar to the sample business card i am sending
front side with lighter back ground (milky colo or light creamr)
instead of cup please insert my logo
details of business:
email, facebook mobile number (larger fonts)

The back of business card
the bacground is white

the van photo(attached)

this text should be printed (enhance your events with a great coffeevan)

```html
<!DOCTYPE html>
<html lang="en">
<head>
<meta charset="utf-8">
<title>Venna Mobile Café – Business Card</title>
<link rel="stylesheet" href="https://fonts.googleapis.com/css2?family=Oswald:wght@500;600&family=Pinyon+Script&display=swap">
<style>
  :root {
    --stage: #ece7df;
    --cream: #fdfbd2;
    --white: #ffffff;
    --espresso: #4a2418;
    --cocoa: #6b3a26;
    --caramel: #a8703f;
    --bean-dark: #3b1e12;
    --bean-mid: #7a4a2c;
    --wood: #b48a5e;
    --van-body: #7b4630;
    --van-light: #c9a27c;
  }
  * { box-sizing: border-box; margin: 0; padding: 0; }
  html, body { width: 1200px; height: 900px; overflow: hidden; }
  body {
    background: var(--stage);
    position: relative;
    font-family: "Oswald", sans-serif;
  }
  .card {
    position: absolute;
    top: 296px;
    width: 540px;
    height: 309px;
    overflow: hidden;
    box-shadow: 0 6px 18px rgba(60, 35, 20, 0.25);
  }
  /* ---------- Front ---------- */
  .card-front { left: 40px; background: var(--cream); }
  .bean-band {
    position: absolute;
    left: 0; right: 0; bottom: 0;
    height: 150px;
    background:
      linear-gradient(180deg, var(--cream) 0%, rgba(253, 251, 210, 0) 38%),
      linear-gradient(180deg, var(--bean-mid) 35%, var(--bean-dark) 62%, var(--wood) 100%);
  }
  .brand {
    position: absolute;
    left: 34px;
    top: 70px;
    width: 200px;
    text-align: center;
  }
  .brand-dot {
    width: 78px; height: 78px;
    margin: 0 auto 10px;
    border-radius: 50%;
    background: var(--caramel);
  }
  .brand-name {
    font-weight: 600;
    font-size: 24px;
    letter-spacing: 0.5px;
    color: var(--espresso);
  }
  .holder-name {
    position: absolute;
    left: 292px;
    top: 48px;
    font-family: "Pinyon Script", cursive;
    font-size: 40px;
    color: var(--cocoa);
  }
  .contact-list {
    position: absolute;
    left: 298px;
    top: 112px;
    list-style: none;
  }
  .contact-item {
    display: flex;
    align-items: center;
    gap: 9px;
    font-weight: 500;
    font-size: 14px;
    letter-spacing: 0.6px;
    line-height: 22px;
    color: var(--espresso);
  }
  .contact-icon { width: 12px; height: 12px; flex: none; }
  /* ---------- Back ---------- */
  .card-back { left: 620px; background: var(--white); }
  .van-art {
    position: absolute;
    left: 212px;
    top: 26px;
    width: 116px;
    height: 112px;
    border-radius: 18px 18px 26px 26px;
    background: linear-gradient(180deg, var(--van-light) 0%, var(--van-body) 55%, var(--espresso) 100%);
  }
  .tagline-band {
    position: absolute;
    left: 0; right: 0;
    top: 176px;
    height: 56px;
    background: var(--caramel);
    display: flex;
    align-items: center;
    justify-content: center;
  }
  .tagline {
    font-family: "Pinyon Script", cursive;
    font-size: 25px;
    color: var(--white);
  }
</style>
</head>
<body>

  <section class="card card-front">
    <div class="bean-band" role="img" aria-label="Photograph of roasted coffee beans scattered on a wooden table"></div>

    <div class="brand">
      <div class="brand-dot"></div>
      <p class="brand-name">Venna Mobile Café</p>
    </div>

    <h1 class="holder-name">John Doe</h1>

    <ul class="contact-list">
      <li class="contact-item">
        <svg class="contact-icon" viewBox="0 0 12 12"><rect x="2.5" y="0.5" width="7" height="11" rx="1.5" fill="none" stroke="#4a2418" stroke-width="1.3"/><circle cx="6" cy="9.4" r="0.8" fill="#4a2418"/></svg>
        444 555 0192
      </li>
      <li class="contact-item">
        <svg class="contact-icon" viewBox="0 0 12 12"><rect x="0.5" y="2" width="11" height="8" fill="#4a2418"/><path d="M0.8 2.4 6 6.6 11.2 2.4" fill="none" stroke="#fdfbd2" stroke-width="1.1"/></svg>
        INFO@VENNACAFE.COM
      </li>
      <li class="contact-item">
        <svg class="contact-icon" viewBox="0 0 12 12"><circle cx="6" cy="6" r="5" fill="#a8703f"/></svg>
        WWW.VENNAPAGE.COM
      </li>
    </ul>
  </section>

  <section class="card card-back">
    <div class="van-art" role="img" aria-label="Illustration of a small brown coffee van with a steaming cup sign on its roof"></div>
    <div class="tagline-band">
      <p class="tagline">Enhance your events with a great coffeevan</p>
    </div>
  </section>

</body>
</html>
```